Wendy Marsh Copywriter Website

I am starting a new business as a freelance copywriter. Trying to set up the website for my business is proving to be too technical for me. I would like a simple, clean website using primarily black and white. I have attached the logo I would like used. I would like the menu icons to be Home, Services, Portfolio, Blog, Contact. I would like my mobile phone number (0412 583 906) and email address (wendy.marsh.copywriter@mailbox-example.com) used in the header of the site. I need the site to be easily manageable and inter-changeable for me to be able to move things around and add images, etc with ease.

I would like the home page to be a static page with space for an image of myself somewhere (I haven't had this taken as yet), an area to put a bit about myself and my business, and also somewhere to include social media icons/links. Again, I would like the whole website and home page to be easily managed so that I can add/delete things with ease.

I would like the image of the typewriter used in the website somewhere also please.

Font styles to use
Sans Serif
Script

Colors
fdf0f6

Requirements
Must have
• The logo provided
• Ability to change page contents easily
• Ability to add social media icons as needed
Nice to have
• Use of the typewriter image
Should not have
• Complicated pages that are not easily editable

```html
<!DOCTYPE html>
<html lang="en">
<head>
<meta charset="utf-8">
<title>Wendy Marsh Copywriter</title>
<link href="https://fonts.googleapis.com/css2?family=Montserrat:wght@400;500;600;700&family=Lato:wght@400;700&family=Libre+Baskerville:wght@400;700&display=swap" rel="stylesheet">
<style>
:root{
  --ink:#111111;
  --white:#ffffff;
  --text:#555555;
  --muted:#8a8a8a;
  --line:#e3e3e3;
  --soft:#f2f2f2;
  --blush:#fdf0f6;
  --dark-band:#232323;
  --sans:"Montserrat",Arial,sans-serif;
  --body:"Lato",Arial,sans-serif;
  --serif:"Libre Baskerville",Georgia,serif;
}
*{margin:0;padding:0;box-sizing:border-box}
html,body{width:1200px;height:4063px;overflow:hidden;background:var(--white);color:var(--ink);font-family:var(--body)}
.page{position:relative;width:1200px;height:4063px}
.abs{position:absolute}
.center{left:0;width:1200px;text-align:center}

/* header */
.topbar{top:0;left:0;width:1200px;height:115px;border-bottom:1px solid var(--line)}
.write-me{left:80px;top:50px;font-family:var(--serif);font-size:13px;color:var(--ink)}
.write-me b{margin-right:10px}
.write-me span{color:var(--text);font-size:12px;font-family:var(--body)}
.brand{left:430px;top:32px;width:400px;text-align:center;font-family:var(--serif);color:var(--ink)}
.brand .name{font-size:30px;letter-spacing:1px;display:block;line-height:36px}
.brand .role{font-size:10px;letter-spacing:6px;text-transform:lowercase;color:var(--text)}
.social{top:36px;width:46px;height:46px;border:1px solid var(--line);border-radius:50%;background:var(--white)}
.nav{top:156px;left:0;width:1200px;display:flex;justify-content:center;gap:0}
.nav a{font-family:var(--serif);font-size:15px;color:#777;text-decoration:none;letter-spacing:1px;text-transform:uppercase;position:absolute}
.nav a.active{color:var(--ink);font-weight:700}

/* hero */
.hero-photo{top:219px;left:0;width:1200px;height:572px;background:linear-gradient(90deg,#f4f4f2 0%,#ecebe8 35%,#d8d6d1 55%,#e8e6e1 80%,#cfd0ce 100%)}
.hero-kicker{left:81px;top:373px;font-family:var(--sans);font-size:19px;color:var(--ink);letter-spacing:.5px}
.hero-title{left:78px;top:410px;font-family:var(--sans);font-size:52px;font-weight:400;color:var(--ink);letter-spacing:.5px}
.hero-title b{font-weight:700}
.hero-text{left:81px;top:486px;width:560px;font-size:15px;line-height:25px;color:#444}
.btn{display:flex;align-items:center;justify-content:center;border-radius:40px;font-family:var(--sans);font-weight:500;text-transform:uppercase;letter-spacing:.5px}
.btn-dark{left:76px;top:561px;width:190px;height:60px;background:var(--ink);color:var(--white);font-size:18px}

/* section headings */
.heading{font-family:var(--sans);font-weight:600;font-size:34px}
.divider{height:10px}
.divider svg{display:block;margin:0 auto}

/* about */
.about-text{left:257px;top:940px;width:686px;text-align:center;font-size:13.5px;line-height:28px;color:var(--text)}
.down-btn{left:577px;top:1070px;width:46px;height:46px;border:1px solid var(--line);border-radius:50%;background:var(--white);display:flex;align-items:center;justify-content:center}

/* services */
.services{top:1178px;left:0;width:1200px;height:518px;background:linear-gradient(180deg,#2a2a2a 0%,#1c1c1c 60%,#262626 100%)}
.services-art{position:absolute;inset:0;background:linear-gradient(120deg,rgba(255,255,255,.06),rgba(0,0,0,.25))}
.service{top:1350px;width:270px;text-align:center;color:var(--white)}
.service .badge{margin:0 auto;display:block}
.service h3{font-family:var(--sans);font-weight:400;font-size:21px;margin-top:22px}
.service p{font-size:13px;line-height:25px;margin-top:14px;color:#e9e9e9;padding:0 24px}

/* portfolio */
.filters{top:1864px;left:0;width:1200px;font-family:var(--serif);font-size:14px;color:#888}
.filters span{position:absolute}
.filters .on{color:var(--ink);font-weight:700}
.grid{top:1929px;left:79px;width:1042px;display:grid;grid-template-columns:repeat(3,1fr);grid-template-rows:repeat(3,217px);column-gap:22px;row-gap:24px}
.tile{position:relative}
.t1{grid-column:1;grid-row:1/3;background:linear-gradient(160deg,#4a4a4a,#2b2b2b)}
.t2{grid-column:2;grid-row:1;background:linear-gradient(180deg,#c9dce6 0%,#e9e3d6 55%,#d8cdb8 100%)}
.t3{grid-column:3;grid-row:1;background:linear-gradient(135deg,#b07a52,#8e5b37 60%,#c49a78)}
.t4{grid-column:2;grid-row:2;background:linear-gradient(135deg,#dcdcdc,#f4f4f4 50%,#9c9c9c)}
.t5{grid-column:3;grid-row:2/4;background:linear-gradient(180deg,#c9cbcc,#e6e6e6 60%,#b9b9b9)}
.t6{grid-column:1;grid-row:3;background:linear-gradient(135deg,#d8d8d8,#a9a9a9 60%,#e9e9e9)}
.t7{grid-column:2;grid-row:3;background:linear-gradient(135deg,#c9a786,#e7d2bd 50%,#8b6b4f)}
.tile-overlay{position:absolute;inset:0;background:rgba(0,0,0,.55);display:flex;flex-direction:column;align-items:center;justify-content:center;color:var(--white)}
.tile-overlay h4{font-family:var(--sans);font-weight:400;font-size:20px;letter-spacing:.5px;margin-bottom:14px}
.tile-overlay .icons{display:flex;gap:14px}

/* blog */
.blog{top:2695px;left:0;width:1200px;height:577px;background:var(--soft)}
.post{top:2866px;width:333px;height:331px;color:var(--white);display:flex;flex-direction:column;align-items:center;justify-content:center;text-align:center}
.post h4{font-family:var(--serif);font-weight:700;font-size:22px;line-height:33px;padding:0 30px}
.post .meta{font-family:var(--sans);font-size:13px;margin-top:14px;display:flex;align-items:center;gap:12px}
.p1{left:79px;background:linear-gradient(160deg,#3d3d3d,#242424)}
.p2{left:434px;background:linear-gradient(160deg,#4a4a4a,#2c2c2c)}
.p3{left:788px;background:linear-gradient(160deg,#525252,#2e2e2e)}

/* contact */
.contact{top:3272px;left:0;width:1200px;height:791px;background:#000}
.contact-item{top:3448px;width:360px;text-align:center;color:var(--white)}
.contact-item .ic{width:60px;height:60px;border-radius:50%;background:var(--white);margin:0 auto;display:flex;align-items:center;justify-content:center}
.contact-item h5{font-family:var(--sans);font-weight:400;font-size:20px;margin-top:14px}
.contact-item p{font-size:14px;line-height:24px;margin-top:4px;font-weight:700}
.field{border:1px solid #cfcfcf;color:var(--white);font-family:var(--serif);font-weight:700;font-size:13px;padding:22px 24px}
.f-name{left:122px;top:3657px;width:466px;height:60px}
.f-email{left:610px;top:3657px;width:468px;height:60px}
.f-msg{left:122px;top:3738px;width:956px;height:106px}
.btn-light{left:507px;top:3866px;width:186px;height:62px;background:var(--white);color:var(--ink);font-size:18px}
.footer-line{left:0;top:3982px;width:1200px;border-top:1px solid #2a2a2a}
.copyright{top:4015px;font-size:12px;color:#cfcfcf}
.copyright b{color:var(--white)}
</style>
</head>
<body>
<div class="page">

  <!-- header -->
  <header class="abs topbar">
    <div class="abs write-me"><b>Write Me :</b><span>wendy.marsh.copywriter@mailbox-example.com</span></div>
    <div class="abs brand"><span class="name">wendy marsh</span><span class="role">copywriter</span></div>
    <a class="abs social" style="left:963px" aria-label="Social link one"></a>
    <a class="abs social" style="left:1025px" aria-label="Social link two"></a>
    <a class="abs social" style="left:1082px" aria-label="Social link three"></a>
  </header>
  <nav class="abs nav">
    <a class="active" style="left:243px">Home</a>
    <a style="left:348px">About Us</a>
    <a style="left:487px">Services</a>
    <a style="left:622px">Portfolio</a>
    <a style="left:772px">Blog</a>
    <a style="left:868px">Contact</a>
  </nav>

  <!-- hero -->
  <section>
    <div class="abs hero-photo" role="img" aria-label="Photo of the copywriter standing at a desk in a bright office, holding a mug"></div>
    <div class="abs hero-kicker">I LOVE TO COPYWRITE</div>
    <h1 class="abs hero-title">I AM <b>WENDY MARSH</b></h1>
    <p class="abs hero-text">A wonderful serenity has taken possession of my entire soul, like these sweet mornings of spring which I enjoy with my whole heart.</p>
    <a class="abs btn btn-dark">Contact Us</a>
  </section>

  <!-- about -->
  <section>
    <h2 class="abs center heading" style="top:848px">few word about WENDY MARSH</h2>
    <div class="abs center divider" style="top:906px"><svg width="90" height="10"><line x1="0" y1="5" x2="90" y2="5" stroke="#cccccc"/><circle cx="45" cy="5" r="3.5" fill="#999"/></svg></div>
    <p class="abs about-text">Lorem Ipsum is simply dummy text of the printing and typesetting industry. Lorem Ipsum has been the industry's standard dummy text ever since the 1500s, when an unknown printer took a galley of type and scrambled it to make a type specimen book.It has survived not only five centuries, but also the leap into electronic typesetting, remaining essentially unchanged.</p>
    <div class="abs down-btn"><svg width="14" height="18" viewBox="0 0 14 18"><path d="M7 2v13M3 11l4 4 4-4" fill="none" stroke="#111" stroke-width="2"/></svg></div>
  </section>

  <!-- services -->
  <section>
    <div class="abs services" role="img" aria-label="Dark close-up photo of typewriter keys"><div class="services-art"></div></div>
    <h2 class="abs center heading" style="top:1236px;color:#fff">Our Services</h2>
    <div class="abs center divider" style="top:1295px"><svg width="90" height="10"><line x1="0" y1="5" x2="90" y2="5" stroke="#bbbbbb"/><circle cx="45" cy="5" r="3.5" fill="#fff"/></svg></div>

    <div class="abs service" style="left:63px">
      <svg class="badge" width="140" height="140" viewBox="0 0 140 140"><rect x="26" y="26" width="88" height="88" transform="rotate(45 70 70)" fill="#fdf0f6" stroke="#fff" stroke-width="4"/><rect x="52" y="54" width="32" height="38" fill="none" stroke="#222" stroke-width="3"/><path d="M66 86l22-26 6 5-22 26-8 2z" fill="#fff" stroke="#222" stroke-width="3"/></svg>
      <h3>Blogging</h3>
      <p>Lorem Ipsum is simply dummy text of the printing and typesetting industry Lorem Ipsum.</p>
    </div>
    <div class="abs service" style="left:331px">
      <svg class="badge" width="140" height="140" viewBox="0 0 140 140"><rect x="26" y="26" width="88" height="88" transform="rotate(45 70 70)" fill="#fdf0f6" stroke="#fff" stroke-width="4"/><rect x="50" y="50" width="40" height="34" fill="none" stroke="#222" stroke-width="3"/><line x1="56" y1="60" x2="84" y2="60" stroke="#222" stroke-width="3"/><circle cx="68" cy="72" r="6" fill="none" stroke="#222" stroke-width="3"/><path d="M60 92h20" stroke="#222" stroke-width="3"/></svg>
      <h3>SEO Articles</h3>
      <p>Lorem Ipsum is simply dummy text of the printing and typesetting industry Lorem Ipsum.</p>
    </div>
    <div class="abs service" style="left:599px">
      <svg class="badge" width="140" height="140" viewBox="0 0 140 140"><rect x="26" y="26" width="88" height="88" transform="rotate(45 70 70)" fill="#fdf0f6" stroke="#fff" stroke-width="4"/><g stroke="#222" stroke-width="2.5" fill="#fff"><line x1="70" y1="70" x2="70" y2="48"/><line x1="70" y1="70" x2="90" y2="62"/><line x1="70" y1="70" x2="88" y2="86"/><line x1="70" y1="70" x2="52" y2="86"/><line x1="70" y1="70" x2="50" y2="62"/><circle cx="70" cy="70" r="6"/><circle cx="70" cy="46" r="4"/><circle cx="92" cy="61" r="4"/><circle cx="90" cy="88" r="4"/><circle cx="50" cy="88" r="4"/><circle cx="48" cy="61" r="4"/></g></svg>
      <h3>Social Copywriting</h3>
      <p>Lorem Ipsum is simply dummy text of the printing and typesetting industry Lorem Ipsum.</p>
    </div>
    <div class="abs service" style="left:865px">
      <svg class="badge" width="140" height="140" viewBox="0 0 140 140"><rect x="26" y="26" width="88" height="88" transform="rotate(45 70 70)" fill="#fdf0f6" stroke="#fff" stroke-width="4"/><rect x="50" y="52" width="40" height="36" fill="none" stroke="#222" stroke-width="3"/><rect x="55" y="57" width="30" height="8" fill="#222"/><g stroke="#222" stroke-width="2.5"><line x1="55" y1="71" x2="68" y2="71"/><line x1="55" y1="77" x2="68" y2="77"/><line x1="55" y1="83" x2="68" y2="83"/><rect x="72" y="70" width="13" height="13" fill="none"/></g></svg>
      <h3>Press Release Writing</h3>
      <p>Lorem Ipsum is simply dummy text of the printing and typesetting industry Lorem Ipsum.</p>
    </div>
  </section>

  <!-- portfolio -->
  <section>
    <h2 class="abs center heading" style="top:1754px">My Portfolio</h2>
    <div class="abs center divider" style="top:1810px"><svg width="20" height="10"><circle cx="10" cy="5" r="3.5" fill="#bbb"/></svg></div>
    <div class="abs filters">
      <span class="on" style="left:396px">All</span>
      <span style="left:457px">Story</span>
      <span style="left:532px">Reading</span>
      <span style="left:635px">Motion</span>
      <span style="left:725px">Inspiration</span>
    </div>
    <div class="abs grid">
      <div class="tile t1" role="img" aria-label="Photo of a dark keyboard with a news key">
        <div class="tile-overlay">
          <h4>READING</h4>
          <div class="icons">
            <svg width="40" height="40" viewBox="0 0 40 40"><circle cx="20" cy="20" r="19" fill="none" stroke="#fff" stroke-width="1.5"/><path d="M10 20q10-10 20 0q-10 10-20 0z" fill="none" stroke="#fff" stroke-width="1.5"/><circle cx="20" cy="20" r="3" fill="#fff"/></svg>
            <svg width="40" height="40" viewBox="0 0 40 40"><circle cx="20" cy="20" r="19" fill="none" stroke="#fff" stroke-width="1.5"/><circle cx="18" cy="18" r="6" fill="none" stroke="#fff" stroke-width="1.8"/><line x1="22.5" y1="22.5" x2="28" y2="28" stroke="#fff" stroke-width="1.8"/></svg>
          </div>
        </div>
      </div>
      <div class="tile t2" role="img" aria-label="Photo of a laptop on a beach towel"></div>
      <div class="tile t3" role="img" aria-label="Photo of newspapers and coffee on a wooden table"></div>
      <div class="tile t4" role="img" aria-label="Photo of a person reading a newspaper at a desk"></div>
      <div class="tile t5" role="img" aria-label="Photo of a white mug beside folded newspapers"></div>
      <div class="tile t6" role="img" aria-label="Photo of a phone resting on newspapers"></div>
      <div class="tile t7" role="img" aria-label="Photo of a person reading a newspaper in a cafe"></div>
    </div>
  </section>

  <!-- blog -->
  <section>
    <div class="abs blog"></div>
    <h2 class="abs center heading" style="top:2756px">Recent Blog</h2>
    <div class="abs center divider" style="top:2812px"><svg width="90" height="10"><line x1="0" y1="5" x2="90" y2="5" stroke="#cccccc"/><circle cx="45" cy="5" r="3.5" fill="#999"/></svg></div>
    <article class="abs post p1" role="img" aria-label="Photo of a person typing on a laptop">
      <h4>The Look of Love: You Will Find It</h4>
      <div class="meta"><span>August 29</span><span>|</span><span>&#9679; 0 Comments</span></div>
    </article>
    <article class="abs post p2" role="img" aria-label="Photo of hands writing at a desk">
      <h4>A Wrong Turn that Leads to Happiness</h4>
      <div class="meta"><span>August 29</span><span>|</span><span>&#9679; 0 Comments</span></div>
    </article>
    <article class="abs post p3" role="img" aria-label="Photo of a person relaxing outdoors with a laptop">
      <h4>Stylists go Crazy for 2016 Summer Season</h4>
      <div class="meta"><span>August 29</span><span>|</span><span>&#9679; 0 Comments</span></div>
    </article>
  </section>

  <!-- contact -->
  <section>
    <div class="abs contact"></div>
    <h2 class="abs center heading" style="top:3329px;color:#fff">Contact Us</h2>
    <div class="abs center divider" style="top:3385px"><svg width="90" height="10"><line x1="0" y1="5" x2="90" y2="5" stroke="#888"/><circle cx="45" cy="5" r="3.5" fill="#fff"/></svg></div>
    <div class="abs contact-item" style="left:56px">
      <div class="ic"><svg width="22" height="28" viewBox="0 0 22 28"><path d="M11 1C5.5 1 1.5 5 1.5 10.5 1.5 18 11 27 11 27s9.5-9 9.5-16.5C20.5 5 16.5 1 11 1z" fill="#000"/><circle cx="11" cy="10.5" r="3.5" fill="#fff"/></svg></div>
      <h5>Address</h5>
      <p>2150 Harbor Lane<br>- Bayview CA</p>
    </div>
    <div class="abs contact-item" style="left:419px">
      <div class="ic"><svg width="26" height="20" viewBox="0 0 26 20"><rect x="1" y="1" width="24" height="18" fill="#000"/><path d="M1 1l12 10L25 1" fill="none" stroke="#fff" stroke-width="2"/></svg></div>
      <h5>Email</h5>
      <p>wendy.marsh.copywriter@mailbox-example.com</p>
    </div>
    <div class="abs contact-item" style="left:784px">
      <div class="ic"><svg width="26" height="26" viewBox="0 0 24 24"><path d="M6.6 10.8c1.4 2.8 3.8 5.1 6.6 6.6l2.2-2.2c.3-.3.7-.4 1-.2 1.1.4 2.3.6 3.6.6.6 0 1 .4 1 1V20c0 .6-.4 1-1 1C10.6 21 3 13.4 3 4c0-.6.4-1 1-1h3.5c.6 0 1 .4 1 1 0 1.3.2 2.5.6 3.6.1.3 0 .7-.2 1z" fill="#000"/></svg></div>
      <h5>Phone</h5>
      <p>0412 583 906</p>
    </div>
    <div class="abs field f-name">Name :</div>
    <div class="abs field f-email">Email :</div>
    <div class="abs field f-msg">Message :</div>
    <a class="abs btn btn-light">Contact Us</a>
    <div class="abs footer-line"></div>
    <p class="abs center copyright">Copyright © <b>WENDY MARSH</b> - 2018 . All Right Reserved</p>
  </section>

</div>
</body>
</html>
```